GLC - New Homepage needed for an existing website

Lantern of Meadows Website
Need a new Homepage for an existing website with Action Items and Newer Pictures
This is the current Website
https://lanternofmeadows.example/

This new page will be changed on Jan 21st when Voting begins
1. Voting like a political campaign where we are trying to raise awareness for the issues we stand for and urge the people to go to a Polling /voting website and vote for us (Roster 47)
2. We have 6 basic themes as to what we stand for - there will be text to promote their importance of voting/call to action
3. There will be videos on the website and there will be a simulation of how the voting process works - will be added later

Use colors like the US Flag - Red, White and Blue. The other pages don't need to be changed - only the HomePage.

I only need the design, I will code the website. Thank you

Target Market(s)

Jewish People in the US

Industry/Entity Type

Religious

Number of Pages Required

1 page

Font styles to use
Serif
Sans Serif

Colors

Designer to choose colors to be used in the design.

Requirements
Must have
• Call to Action - Go out to Vote
• This is the current Website - https://lanternofmeadows.example/

```html
<!DOCTYPE html>
<html lang="en">
<head>
<meta charset="utf-8">
<title>Lantern of Meadows — Jewish Continuity</title>
<link rel="stylesheet" href="https://fonts.googleapis.com/css2?family=Poppins:ital,wght@0,300;0,400;0,500;0,700;0,800;1,400&family=Roboto:wght@400;500;700&family=Merriweather:wght@700;900&display=swap">
<style>
:root{
  --navy:#0f2a6b;
  --navy-deep:#0c2463;
  --red:#d7132a;
  --red-soft:#e01f35;
  --ink:#1d1d1f;
  --text:#5a5a5a;
  --white:#ffffff;
  --field:#ececec;
  --wall:#f2f2f2;
  --quote-mark:#b9c4d6;
}
*{box-sizing:border-box;margin:0;padding:0}
html,body{width:1200px;height:3064px;overflow:hidden}
body{position:relative;background:var(--white);font-family:"Poppins",sans-serif;color:var(--ink)}
.abs{position:absolute}

/* header */
.site-header{position:absolute;left:0;top:0;width:1200px;height:82px;background:var(--white);border-bottom:1px solid #e6e6e6}
.brand{position:absolute;left:168px;top:27px;display:flex;align-items:center;gap:8px;font-family:"Roboto",sans-serif;font-weight:700;font-size:15px;color:var(--navy)}
.brand-dot{width:14px;height:14px;border-radius:50%;background:var(--red)}
.main-nav a{position:absolute;top:37px;font-family:"Roboto",sans-serif;font-size:13.5px;font-weight:500;color:#333;text-decoration:none;letter-spacing:.3px}
.btn-join{position:absolute;left:890px;top:26px;width:155px;height:37px;border-radius:19px;background:var(--navy);color:var(--white);font-family:"Roboto",sans-serif;font-weight:500;font-size:13.5px;display:flex;align-items:center;justify-content:center;letter-spacing:.4px}

/* hero */
.hero{position:absolute;left:0;top:82px;width:1200px;height:497px;background:linear-gradient(180deg,#2c7cc8 0%,#4c97d6 45%,#8fc0e6 80%,#cfe2f1 100%);overflow:hidden}
.hero-photo{position:absolute;right:0;top:0;width:530px;height:497px;background:linear-gradient(110deg,rgba(255,255,255,0) 0%,#c9ccd2 35%,#eceef1 60%,#b6bac2 100%)}
.hero-flag{position:absolute;left:680px;top:120px;width:180px;height:110px;background:linear-gradient(120deg,#1f3f8f 0 35%,#c8283b 35% 100%);opacity:.85;border-radius:4px}
.eyebrow{position:absolute;left:156px;top:124px;display:flex;align-items:center;gap:10px;font-family:"Roboto",sans-serif;font-size:13.5px;font-weight:500;color:var(--white);letter-spacing:.4px}
.eyebrow::before{content:"";width:32px;height:1px;background:var(--white)}
.hero-kicker{position:absolute;left:155px;top:160px;font-weight:800;font-size:24px;color:var(--white)}
.hero-title{position:absolute;left:154px;top:192px;font-weight:800;font-size:47px;color:var(--navy-deep);letter-spacing:.2px}
.hero-sub{position:absolute;left:157px;top:272px;font-family:"Roboto",sans-serif;font-size:15px;color:var(--white);letter-spacing:.3px}
.btn-vote{position:absolute;left:152px;top:335px;width:267px;height:62px;border-radius:31px;background:var(--red);display:flex;align-items:center;justify-content:center;gap:16px;font-family:"Merriweather",serif;font-weight:900;font-size:17px;color:var(--white);letter-spacing:.3px}

/* mission */
.mission-art{position:absolute;left:150px;top:640px;width:411px;height:353px}
.mission-title{position:absolute;left:589px;top:662px;font-weight:700;font-size:33px;color:#222;letter-spacing:.3px}
.mission-kicker{position:absolute;left:591px;top:712px;font-family:"Roboto",sans-serif;font-weight:700;font-size:15.5px;color:var(--red);letter-spacing:.3px}
.mission-copy{position:absolute;left:592px;top:768px;width:447px;font-size:13px;line-height:24px;color:var(--text);font-weight:300}
.mission-copy p{margin-bottom:24px}
.pull-quote{position:absolute;left:150px;top:1030px;width:380px;text-align:center;font-family:"Roboto",sans-serif;font-weight:500;font-size:13.5px;line-height:24px;color:var(--navy);letter-spacing:.2px}
.qmark{position:absolute;font-family:"Merriweather",serif;font-weight:900;color:var(--quote-mark);line-height:1}

/* objectives */
.obj-title{position:absolute;left:0;width:1276px;top:1160px;text-align:center;font-weight:800;font-size:30px;color:#1b1b1b;letter-spacing:.4px}
.obj-stats{position:absolute;left:0;width:1200px;top:1216px;display:flex;justify-content:center;gap:46px;font-family:"Roboto",sans-serif;font-weight:500;font-size:20px;color:#1b1b1b;padding-left:60px}
.obj-stats b{color:var(--red);font-size:29px;font-weight:500;margin-right:8px}
.cards{position:absolute;left:0;top:1312px;width:1200px;height:365px}
.card{position:absolute;top:0;height:365px;overflow:hidden}
.card-label{position:absolute;left:22px;bottom:20px;font-family:"Roboto",sans-serif;font-weight:500;font-size:15.5px;line-height:24px;color:var(--white)}
.card-featured{position:absolute;left:397px;top:1293px;width:202px;height:402px;background:var(--navy);color:var(--white);padding:100px 22px 0 20px;font-family:"Roboto",sans-serif}
.card-featured h3{font-weight:500;font-size:16px;line-height:24px;margin-bottom:14px}
.card-featured p{font-size:11.5px;line-height:19.5px}
.btn-discover{position:absolute;left:17px;top:325px;width:110px;height:34px;border:1px solid var(--white);border-radius:17px;display:flex;align-items:center;justify-content:center;font-size:11.5px}

/* video + testimonial */
.wall{position:absolute;left:0;top:1695px;width:1200px;height:481px;background:var(--wall)}
.video{position:absolute;left:157px;top:1792px;width:432px;height:290px;background:linear-gradient(135deg,#5e6f93 0%,#3f5283 55%,#6a6f8e 100%)}
.play{position:absolute;left:331px;top:1908px;width:60px;height:60px;border-radius:50%;background:var(--white);display:flex;align-items:center;justify-content:center}
.avatar{position:absolute;left:789px;top:1812px;width:92px;height:92px;border-radius:50%;border:3px solid var(--red);background:radial-gradient(circle at 50% 40%,#c89a74,#6b4631)}
.testimonial{position:absolute;left:670px;top:1926px;width:355px;text-align:center;font-style:italic;font-size:14.5px;line-height:32px;color:#333}
.testimonial-name{position:absolute;left:670px;top:2036px;width:336px;text-align:center;font-family:"Roboto",sans-serif;font-weight:500;font-size:14px;color:#222;letter-spacing:.3px}

/* join */
.join{position:absolute;left:0;top:2176px;width:1200px;height:508px;background:linear-gradient(135deg,#d11a30 0%,#de2236 50%,#d11a2e 100%)}
.join h2{position:absolute;left:0;width:1200px;top:72px;text-align:center;font-weight:800;font-size:28.5px;color:var(--white);letter-spacing:.4px}
.join-lead{position:absolute;left:0;width:1200px;top:120px;text-align:center;font-size:15px;line-height:30px;color:var(--white)}
.field{position:absolute;width:355px;height:62px;background:var(--field);padding-left:25px;display:flex;align-items:center;font-size:14.5px;color:#8a8a8a}
.btn-action{position:absolute;left:482px;top:405px;width:236px;height:49px;background:var(--navy-deep);display:flex;align-items:center;justify-content:center;gap:16px;font-family:"Merriweather",serif;font-weight:900;font-size:17px;color:var(--white);letter-spacing:.3px}

/* footer */
.site-footer{position:absolute;left:0;top:2684px;width:1200px;height:380px;background:var(--navy-deep);color:var(--white)}
.footer-brand{position:absolute;left:157px;top:62px;display:flex;align-items:center;gap:8px;font-family:"Roboto",sans-serif;font-weight:700;font-size:15px}
.footer-brand .brand-dot{background:var(--white)}
.footer-title{position:absolute;left:157px;top:150px;font-family:"Merriweather",serif;font-weight:700;font-size:17px;letter-spacing:.6px}
.footer-about{position:absolute;left:157px;top:195px;width:330px;font-size:13px;line-height:24px;font-weight:300}
.links-title{position:absolute;left:546px;top:52px;font-weight:700;font-size:18px;letter-spacing:.3px}
.link-col{position:absolute;top:100px;list-style:none;font-size:13px;font-weight:300}
.link-col li{height:36px;display:flex;gap:12px}
.link-col li::before{content:"›";opacity:.9}
.copyright{position:absolute;left:0;width:1200px;top:343px;text-align:center;font-size:9.5px;color:#7d8fbc}
</style>
</head>
<body>

<header class="site-header">
  <div class="brand"><span class="brand-dot"></span>Lantern of Meadows</div>
  <nav class="main-nav">
    <a style="left:457px">HOME</a>
    <a style="left:536px">OUR OBJECTIVES</a>
    <a style="left:682px">MISSON</a>
    <a style="left:762px">PRIVACY POLICY</a>
  </nav>
  <div class="btn-join">JOIN US NOW</div>
</header>

<section class="hero">
  <div class="hero-photo" role="img" aria-label="Photo of the Capitol dome with a flagpole"></div>
  <div class="hero-flag" role="img" aria-label="American flag waving"></div>
  <div class="eyebrow">WELCOME</div>
  <div class="hero-kicker">IT'S ALL ABOUT</div>
  <h1 class="hero-title">JEWISH CONTINUITY</h1>
  <div class="hero-sub">WE EMBRACE OUR PAST TO ENSURE OUR FUTURE</div>
  <div class="btn-vote">
    <svg width="36" height="30" viewBox="0 0 36 30"><rect x="2" y="16" width="32" height="12" fill="#fff"/><rect x="0" y="14" width="36" height="3" fill="#fff"/><rect x="11" y="2" width="14" height="13" fill="#fff" transform="rotate(-12 18 8)"/><rect x="9" y="14" width="18" height="2" fill="#d7132a"/></svg>
    GO OUT TO VOTE
  </div>
</section>

<section class="mission">
  <svg class="mission-art" viewBox="0 0 411 353" role="img" aria-label="Portrait of a smiling young woman inside a triangular frame">
    <defs><linearGradient id="mg" x1="0" y1="0" x2="1" y2="1"><stop offset="0" stop-color="#b88a5c"/><stop offset=".55" stop-color="#8b5d3b"/><stop offset="1" stop-color="#3d4c72"/></linearGradient></defs>
    <polygon points="205,0 411,353 0,353" fill="url(#mg)"/>
  </svg>
  <span class="qmark" style="left:150px;top:1012px;font-size:46px">“</span>
  <div class="pull-quote">BY CONNECTING JEWS TO THEIR HERITAGE,<br>HISTORY AND FAITH, WE CAN ENSTURE THAT GLOBAL<br>JEWRY NOT ONLY SURVIVES, BUT SURGES.</div>
  <span class="qmark" style="left:512px;top:1078px;font-size:46px">”</span>

  <h2 class="mission-title">LANTERN OF MEADOWS</h2>
  <div class="mission-kicker">MISSION STATEMENT</div>
  <div class="mission-copy">
    <p>Lantern of Meadows is a grassroots movement that was established to promote Jewish Continuity, recognizing that in the United States, Judaism and its continuity are under attack for a host of reasons, all of which Lantern of Meadows believes must be identified.</p>
    <p>Lantern of Meadows is non-political. We believe that all American Jews, regardless of ideological belief, can embrace the concept that in order to ensure the survival of the Jewish people there must be Jewish people.</p>
    <p>At the annual Passover Seder we say that “in every generation they stand ready to annihilate us ” - this is both historically accurate and currently relevant.</p>
  </div>
</section>

<section class="objectives">
  <h2 class="obj-title">OUR OBJECTIVES</h2>
  <div class="obj-stats"><span><b>6</b>POINTS.</span><span><b>5</b>MINUTES.</span><span><b>1</b>BOLD NEW MOVEMENT.</span></div>
  <div class="cards">
    <div class="card" style="left:0;width:198px;background:linear-gradient(180deg,#8a6a3a,#3a2a1a)" role="img" aria-label="Star of David at sunset"><div class="card-label">Resist<br>Assimilation</div></div>
    <div class="card" style="left:198px;width:199px;background:linear-gradient(180deg,#4a5f9a,#3a3a48)" role="img" aria-label="Blue kippah with Star of David"><div class="card-label">Confront<br>Anti-Semitism</div></div>
    <div class="card" style="left:599px;width:200px;background:linear-gradient(180deg,#9a8c80,#5e4a3e)" role="img" aria-label="Young man wearing a kippah"><div class="card-label">Instill Jewish<br>Pride</div></div>
    <div class="card" style="left:799px;width:200px;background:linear-gradient(180deg,#b8b0a0,#6e6250)" role="img" aria-label="Model of the ancient Temple"><div class="card-label" style="left:19px">Israel: The Eternal<br>Jewish Homeland</div></div>
    <div class="card" style="left:999px;width:201px;background:linear-gradient(180deg,#6a5040,#2e2018)" role="img" aria-label="Grandmother and granddaughter celebrating"><div class="card-label">Maintain Israel's<br>Jewish Identity</div></div>
  </div>
  <div class="card-featured">
    <h3>Expose<br>BDS</h3>
    <p>BDS has not yet gained enough traction to be &nbsp;a real threat currently, but the threat of BDS looms large when considering the left-leaning American college environment.</p>
    <div class="btn-discover">Discover More</div>
  </div>
</section>

<section class="wall">
</section>
<div class="video" role="img" aria-label="Video still of pencils and small American flags on a desk"></div>
<div class="play"><svg width="18" height="20" viewBox="0 0 18 20"><polygon points="2,1 17,10 2,19" fill="#d7132a"/></svg></div>
<span class="qmark" style="left:720px;top:1838px;font-size:86px">“</span>
<div class="avatar" role="img" aria-label="Portrait photo of a supporter"></div>
<span class="qmark" style="left:888px;top:1838px;font-size:86px">”</span>
<div class="testimonial">By Connecting Jews To Their Heritage, History And Faith, We Can Ensture That Global Jewry Not Only Survives, But Surges.</div>
<div class="testimonial-name">LANTERN OF MEADOWS</div>

<section class="join">
  <h2>JOIN THE JEWISH FUTURE</h2>
  <div class="join-lead">Help us ensure a world Jewish platform that keeps our people<br>and communities strong, safe and proud.</div>
  <div class="field" style="left:232px;top:208px">Name *</div>
  <div class="field" style="left:611px;top:208px">Email Address *</div>
  <div class="field" style="left:232px;top:288px">Cell Phone *</div>
  <div class="field" style="left:611px;top:288px">City *</div>
  <div class="btn-action">
    <svg width="32" height="27" viewBox="0 0 36 30"><rect x="2" y="16" width="32" height="12" fill="#fff"/><rect x="0" y="14" width="36" height="3" fill="#fff"/><rect x="11" y="2" width="14" height="13" fill="#fff" transform="rotate(-12 18 8)"/><rect x="9" y="14" width="18" height="2" fill="#0c2463"/></svg>
    TAKE ACTION
  </div>
</section>

<footer class="site-footer">
  <div class="footer-brand"><span class="brand-dot"></span>Lantern of Meadows</div>
  <div class="footer-title">JEWISH CONTINUITY</div>
  <p class="footer-about">Israel is the geographical anchor of Judaism, the Torah is the &nbsp;deological/theological anchor of Judaism</p>
  <div class="links-title">QUICK LINKS</div>
  <ul class="link-col" style="left:546px">
    <li>Home</li><li>Resist Assimilation</li><li>Confront Anti-Semitism</li><li>Expose BDS</li><li>Instill Jewish Pride</li>
  </ul>
  <ul class="link-col" style="left:795px">
    <li>Israel: The Eternal Jewish Homeland</li><li>Maintain Israel's Jewish Identity</li><li>New Law Increases Hate Crimes</li><li>Privacy Policy</li>
  </ul>
  <div class="copyright">Copyright © 2020 Lantern of Meadows &nbsp;| &nbsp;Privacy Policy</div>
</footer>

</body>
</html>
```